Personal website: Intro to a software engineer, filmmaker, entrepreneur

I'm looking to do a redesign of my website. It's had many forms over the years, primarily because it's been hard to pin down all what I want to communicate. I'm a software engineer, filmmaker, writer, and entrepreneur. I'm looking to showcase not only what I've done and what I can do, but also who I am, what I'm interested in, and what I have to say. The minimal content at this point would be: Name, photo of me, short intro, publications on Tarnly (title, description, date), and social links. In the future I could see adding notable projects, open source contributions, and possibly skills. Think of it as an intro to Dane Colpitt.

I would like this to be all on one page. If I were to pin down the design atheistic I'm going for it would be: Warm, sophisticated, simple, clear, minimal, creative, flat, thoughtful, artistic, and soft. I imagine typography taking more over a role here than images. I know a lot of design is image focused, but I'd rather any photos be accents than main content.

I'm more than happy to give more details if more is needed/wanted.
Updates

Designs look the same

Target Market(s)

Fellow co-creators

Number of Pages Required

1 page

Requirements
Must have
• Name, photo of me, short intro, publications on Tarnly (title, description, date), and social links.
Nice to have
• Notable projects, open source contributions, and skills
Should not have
• It should not be overly techy. I'm about building solutions and sharing ideas.
• Should not look corporate.

```html
<!DOCTYPE html>
<html lang="en">
<head>
<meta charset="utf-8">
<title>Dane Colpitt</title>
<link rel="stylesheet" href="https://fonts.googleapis.com/css2?family=Montserrat:wght@400;500;600;700&display=swap">
<style>
:root{
  --teal:#12a6a9;
  --teal-dark:#0f9598;
  --ink:#2b2b2b;
  --text:#555;
  --muted:#777;
  --paper:#ffffff;
  --mist:#f2f2f2;
  --line:#cfcfcf;
  --footer:#2c2c2c;
}
*{box-sizing:border-box;margin:0;padding:0}
html,body{width:1200px;height:3141px;overflow:hidden}
body{font-family:"Montserrat",sans-serif;color:var(--ink);background:var(--paper);position:relative}
section,header,footer{position:absolute;left:0;width:1200px}
.abs{position:absolute}
.btn{position:absolute;display:flex;align-items:center;justify-content:center;background:var(--teal);color:#fff;border-radius:22px;font-weight:600;font-size:14px}

/* hero */
.hero{top:0;height:580px;overflow:hidden}
.hero-photo{position:absolute;inset:0;background:linear-gradient(100deg,#3a3f42 0%,#585c5c 40%,#6b6a66 60%,#3d3f3f 100%)}
.hero-shade{position:absolute;inset:0;background:linear-gradient(90deg,rgba(0,0,0,.45),rgba(0,0,0,.1) 60%,rgba(0,0,0,.3))}
.brand{left:88px;top:36px;color:#fff;font-size:29px;font-weight:700;letter-spacing:.5px}
.nav{left:515px;top:43px;display:flex;gap:41px;color:#fff;font-size:15px;font-weight:500}
.search{left:1083px;top:40px}
.hero-title{left:88px;top:194px;color:#fff;font-size:31px;font-weight:700}
.hero-sub{left:92px;top:254px;width:340px;color:#fff;font-size:16px;line-height:26px}
.hero-curve{position:absolute;left:0;bottom:0}
.dots{left:569px;top:508px;display:flex;gap:12px;align-items:center}
.dots span{width:11px;height:11px;border-radius:50%;background:#fff}
.dots .on{width:18px;height:18px;background:transparent;border:2px solid #fff;display:flex;align-items:center;justify-content:center}
.dots .on::after{content:"";width:9px;height:9px;border-radius:50%;background:#fff}

/* about */
.about{top:565px;height:457px;background:var(--mist)}
.portrait{left:91px;top:64px;width:330px;height:330px;border-radius:50%;background:radial-gradient(circle at 50% 45%,#4a4a4a,#1f1f1f 70%)}
.portrait-ring{position:absolute;left:15px;top:15px;width:300px;height:300px;border-radius:50%;border:2px dashed rgba(255,255,255,.85)}
.section-title{color:var(--teal);font-weight:700;font-size:34px}
.about-title{left:553px;top:68px}
.about-sub{left:553px;top:118px;font-size:20px;color:#444;font-weight:500}
.about-text{left:553px;top:163px;width:560px;font-size:14.5px;line-height:27px;color:var(--text)}

/* skills */
.skills{top:1022px;height:586px;background:var(--paper)}
.center-title{left:0;width:1200px;text-align:center}
.skill{top:144px;width:302px;height:254px;background:#fff;box-shadow:0 2px 12px rgba(0,0,0,.14);text-align:center;padding-top:38px}
.skill svg{display:block;margin:0 auto}
.skill h3{font-size:20px;font-weight:500;margin-top:18px;color:#333}
.skill p{font-size:14.5px;line-height:24px;color:var(--muted);margin:10px auto 0;width:230px}
.skill.active{background:var(--teal);color:#fff}
.skill.active h3,.skill.active p{color:#fff}
.chev{margin-top:6px !important}

/* projects */
.projects{top:1608px;height:616px;background:var(--mist)}
.projects-title{left:86px;top:70px}
.projects-sub{left:88px;top:124px;font-size:15px;color:#444}
.card{top:176px;width:316px;height:362px;background:#fff}
.card-img{position:absolute;left:0;top:0;width:316px;height:178px}
.date{position:absolute;left:0;top:0;width:48px;text-align:center;font-size:12px}
.date b{display:block;background:var(--teal);color:#fff;font-size:17px;height:28px;line-height:28px}
.date i{display:block;background:#e8e8e8;color:#555;font-style:normal;height:22px;line-height:22px}
.card h4{position:absolute;left:14px;top:200px;font-size:16.5px;font-weight:600;color:#222}
.card p{position:absolute;left:14px;top:234px;width:290px;font-size:14.5px;line-height:22.5px;color:var(--text)}
.card .more{position:absolute;right:22px;bottom:10px;font-size:16px;color:#222;font-weight:500}
.card.active h4,.card.active .more{color:var(--teal)}
.card.active{border-bottom:3px solid var(--teal)}

/* contributions */
.contrib{top:2224px;height:746px;background:var(--paper)}
.contrib-title{top:42px}
.timeline{left:0;top:154px;width:1200px;height:80px}
.activity{left:0;width:1200px;top:294px;text-align:center;color:var(--teal);font-size:19px;font-weight:500}
.month{left:274px;top:348px;color:var(--teal);font-size:17px;font-weight:500}
.jump{left:842px;top:348px;color:#444;font-size:17px}
.acc{left:274px;width:662px;background:var(--teal);color:#fff;font-size:15px;font-weight:600;display:flex;justify-content:space-between;align-items:center;padding:0 28px}
.acc-body{left:274px;top:444px;width:662px;height:42px;border:1px solid #ddd;border-top:none;font-size:13px;color:#555;display:flex;align-items:center;padding-left:28px;background:#fff}

/* footer */
.footer{top:2970px;height:171px;background:var(--footer);color:#fff}
.footer-nav{left:0;width:1200px;top:36px;display:flex;justify-content:center;gap:40px;font-size:15px}
.social{left:0;width:1200px;top:83px;display:flex;justify-content:center;gap:12px}
.social span{width:29px;height:29px;border-radius:50%;background:#fff}
.copy{left:0;width:1200px;top:126px;text-align:center;font-size:13px}
</style>
</head>
<body>

<header class="hero">
  <div class="hero-photo" role="img" aria-label="Photo of Dane Colpitt standing with arms crossed in a bright office, colleagues talking behind"></div>
  <div class="hero-shade"></div>
  <div class="abs brand">DANE COLPITT</div>
  <nav class="abs nav"><span>Home</span><span>About Me</span><span>Skills</span><span>Projects</span><span>Contributions</span></nav>
  <svg class="abs search" width="20" height="20" viewBox="0 0 20 20"><circle cx="8" cy="8" r="6" fill="none" stroke="#fff" stroke-width="2"/><line x1="12.5" y1="12.5" x2="18" y2="18" stroke="#fff" stroke-width="2.4"/></svg>
  <h1 class="abs hero-title">HI! I'm DANE COLPITT</h1>
  <p class="abs hero-sub">I'm a Software Engineer, Filmmaker &amp; Entrepreneur.</p>
  <div class="btn" style="left:88px;top:325px;width:124px;height:40px">Read More</div>
  <svg class="hero-curve" width="1200" height="200" viewBox="0 0 1200 200"><path d="M0,50 Q620,330 1200,0 L1200,200 L0,200 Z" fill="#fff"/></svg>
  <div class="abs dots"><span class="on"></span><span></span><span></span></div>
</header>

<section class="about">
  <div class="abs portrait" role="img" aria-label="Portrait photo of Dane Colpitt"><div class="portrait-ring"></div></div>
  <h2 class="abs section-title about-title">About Me !</h2>
  <div class="abs about-sub">I'm Dane Colpitt</div>
  <p class="abs about-text">Lorem ipsum dolor sit amet, consectetur adipiscing elit, sed do eiusmod tempor incididunt ut labore et dolore magna aliqua. Ut enim ad minim veniam, quis nostrud exercitation ullamco laboris nisi ut aliquip ex ea commodo consequat. Duis aute irure dolor in reprehenderit in voluptate velit esse cillum dolore eu fugiat nulla pariatur.</p>
  <div class="btn" style="left:553px;top:324px;width:124px;height:38px">Read More</div>
</section>

<section class="skills">
  <h2 class="abs section-title center-title" style="top:58px">Our Skills</h2>
  <div class="abs skill" style="left:124px">
    <svg width="76" height="70" viewBox="0 0 76 70" fill="none" stroke="#333" stroke-width="2"><rect x="22" y="4" width="48" height="34"/><line x1="46" y1="38" x2="46" y2="48"/><line x1="36" y1="48" x2="56" y2="48"/><circle cx="46" cy="21" r="7"/><circle cx="46" cy="21" r="2.5"/><circle cx="16" cy="46" r="10"/><rect x="6" y="58" width="24" height="8"/><circle cx="62" cy="60" r="5"/></svg>
    <h3>Software Engineer</h3>
    <p>Sed ut perspiciatis unde omnis iste natus error sit</p>
  </div>
  <div class="abs skill active" style="left:448px">
    <svg width="76" height="70" viewBox="0 0 76 70" fill="none" stroke="#fff" stroke-width="2"><rect x="6" y="12" width="64" height="44"/><line x1="6" y1="22" x2="70" y2="22"/><line x1="6" y1="46" x2="70" y2="46"/><rect x="16" y="26" width="18" height="16"/><rect x="42" y="26" width="18" height="16"/><g stroke-width="1.5"><line x1="14" y1="14" x2="14" y2="20"/><line x1="24" y1="14" x2="24" y2="20"/><line x1="34" y1="14" x2="34" y2="20"/><line x1="44" y1="14" x2="44" y2="20"/><line x1="54" y1="14" x2="54" y2="20"/><line x1="64" y1="14" x2="64" y2="20"/><line x1="14" y1="48" x2="14" y2="54"/><line x1="24" y1="48" x2="24" y2="54"/><line x1="34" y1="48" x2="34" y2="54"/><line x1="44" y1="48" x2="44" y2="54"/><line x1="54" y1="48" x2="54" y2="54"/><line x1="64" y1="48" x2="64" y2="54"/></g></svg>
    <h3>Film Maker</h3>
    <p>Sed ut perspiciatis unde omnis iste natus error sit</p>
    <svg class="chev" width="18" height="18" viewBox="0 0 18 18" fill="none" stroke="#fff" stroke-width="1.4"><circle cx="9" cy="9" r="8"/><polyline points="5.5,7.5 9,11 12.5,7.5"/></svg>
  </div>
  <div class="abs skill" style="left:773px">
    <svg width="76" height="70" viewBox="0 0 76 70" fill="none" stroke="#333" stroke-width="2"><rect x="10" y="26" width="26" height="20"/><line x1="10" y1="34" x2="36" y2="34"/><rect x="18" y="20" width="10" height="6"/><rect x="40" y="38" width="22" height="26"/><circle cx="58" cy="16" r="11"/><circle cx="58" cy="16" r="4"/><line x1="20" y1="46" x2="20" y2="66"/><line x1="28" y1="46" x2="28" y2="66"/></svg>
    <h3>Entrepreneur</h3>
    <p>Sed ut perspiciatis unde omnis iste natus error sit</p>
    <svg class="chev" width="18" height="18" viewBox="0 0 18 18" fill="none" stroke="#555" stroke-width="1.4"><circle cx="9" cy="9" r="8"/><polyline points="5.5,7.5 9,11 12.5,7.5"/></svg>
  </div>
  <div class="btn" style="left:512px;top:453px;width:188px;height:44px;font-size:15px">View More Skills</div>
</section>

<section class="projects">
  <h2 class="abs section-title projects-title">Our Projects</h2>
  <p class="abs projects-sub">Lorem ipsum dolor sit amet, consectetur adipisicing elit. Distinctio nobis</p>
  <article class="abs card" style="left:86px">
    <div class="card-img" role="img" aria-label="Man in a suit sitting outside a glass office building" style="background:linear-gradient(160deg,#9fb4bd,#6f8570 60%,#4a5a48)"></div>
    <div class="date"><b>28</b><i>Aug</i></div>
    <h4>Dignissim phasellus ultrices tellus</h4>
    <p>Sed odio orci, fringilla nec dolor et, euismod auctor mauris. Curabitur semper dui diam, nec accumsan mauris consequat sed.</p>
    <span class="more">Read More</span>
  </article>
  <article class="abs card active" style="left:442px">
    <div class="card-img" role="img" aria-label="Film camera and clapperboard on a dark set" style="background:linear-gradient(135deg,#1e1e1e,#3a3a3a 50%,#8a8070)"></div>
    <div class="date"><b>28</b><i>Aug</i></div>
    <h4>Dignissim phasellus ultrices tellus</h4>
    <p>Sed odio orci, fringilla nec dolor et, euismod auctor mauris. Curabitur semper dui diam, nec accumsan mauris consequat sed.</p>
    <span class="more">Read More</span>
  </article>
  <article class="abs card" style="left:796px">
    <div class="card-img" role="img" aria-label="Person working at a desk in a bright white office" style="background:linear-gradient(135deg,#e9ecec,#c9cfcf 55%,#8d9596)"></div>
    <div class="date"><b>28</b><i>Aug</i></div>
    <h4>Dignissim phasellus ultrices tellus</h4>
    <p>Sed odio orci, fringilla nec dolor et, euismod auctor mauris. Curabitur semper dui diam, nec accumsan mauris consequat sed.</p>
    <span class="more">Read More</span>
  </article>
</section>

<section class="contrib">
  <h2 class="abs section-title center-title contrib-title">Contributions</h2>
  <svg class="abs timeline" viewBox="0 0 1200 80" width="1200" height="80" font-family="Montserrat, sans-serif" font-size="18" font-weight="600" text-anchor="middle">
    <line x1="212" y1="40" x2="981" y2="40" stroke="#d6d6d6" stroke-width="1.5"/>
    <circle cx="199" cy="40" r="12" fill="#fff" stroke="var(--teal)" stroke-width="2"/>
    <circle cx="993" cy="40" r="12" fill="#fff" stroke="var(--teal)" stroke-width="2"/>
    <circle cx="329" cy="40" r="36" fill="#fff" stroke="var(--teal)" stroke-width="3"/><text x="329" y="46" fill="var(--teal)">2017</text>
    <circle cx="432" cy="40" r="36" fill="#fff" stroke="#333" stroke-width="2"/><text x="432" y="46" fill="#333">2016</text>
    <circle cx="536" cy="40" r="36" fill="#fff" stroke="#333" stroke-width="2"/><text x="536" y="46" fill="#333">2015</text>
    <circle cx="641" cy="40" r="36" fill="#fff" stroke="#333" stroke-width="2"/><text x="641" y="46" fill="#333">2014</text>
    <circle cx="746" cy="40" r="36" fill="#fff" stroke="#333" stroke-width="2"/><text x="746" y="46" fill="#333">2013</text>
    <circle cx="857" cy="40" r="36" fill="#fff" stroke="#333" stroke-width="2"/><text x="857" y="46" fill="#333">2012</text>
  </svg>
  <div class="abs activity">Contribution Activity</div>
  <div class="abs month">November</div>
  <div class="abs jump">Jump To &nbsp;<span style="font-size:11px">▾</span></div>
  <div class="abs acc" style="top:387px;height:57px"><span>Created 7 Commits in Repository</span><span>-</span></div>
  <div class="abs acc-body">dcolpitt/danecolpitt.com 7 commits</div>
  <div class="abs acc" style="top:488px;height:56px"><span>Created 10 Repository</span><span style="font-size:20px">+</span></div>
  <div class="abs acc" style="top:546px;height:57px"><span>163 Contributions In Private Repositories</span><span style="font-size:20px">+</span></div>
  <div class="btn" style="left:522px;top:643px;width:154px;height:46px;border-radius:24px;font-size:15px">Load More</div>
</section>

<footer class="footer">
  <nav class="abs footer-nav"><span>Home</span><span>About Me</span><span>Skills</span><span>Projects</span><span>Contributions</span></nav>
  <div class="abs social" aria-label="Social links"><span></span><span></span><span></span><span></span></div>
  <p class="abs copy">© 2018 Copyrights | All Rights Reserved</p>
</footer>

</body>
</html>
```